VARNEK Consulting Services “Coming Soon” Landing Page

MORE INTO IN Design Brief for Web Designer document attached

1. Project Overview
Client: VARNEK Consulting Services
Project: Build a static, responsive “Coming Soon” landing page (HTML/CSS/JS)
Timeline: Target launch date in June 7, 2025
Point of Contact: Martin Holloway (Managing Director)
 • Email: martin@varnekconsulting.com
 • Phone: 555-304-7728
Background:
VARNEK Consulting Services is a boutique IT consultancy specializing in enterprise cloud solutions, microservices, FlowMesh migrations, and AGENTIC AI-driven integrations. We are launching a new website to capture CIO-level leads, build brand awareness, and communicate our key value propositions before the full site goes live. This “Coming Soon” page should reflect our brand identity, target CIO and enterprise IT leaders, and collect email addresses for early access to whitepapers, case studies, and consultations.

2. Goals & Objectives
1. Brand Reinforcement
• Convey a contemporary, corporate, and professional look that aligns with VARNEK’s positioning as a specialized, agile, high-ROI consultancy.
• Utilize our brand colors (green, red, blue, gold) and typography (Segoe UI) consistently.
2. Lead Generation
• Implement a simple email-capture form (“Notify Me”) that submits to mailto:info@varnekconsulting.com.
• Convey clear messaging so visitors understand why they should sign up (exclusive early insights, whitepapers, invitations to consult).
3. Enterprise Leadership-Focused Messaging
• Immediately communicate our core value proposition (“Enterprise Modernization Reimagined”) and differentiation versus larger consulting firms.
• Introduce AGENTIC AI use cases to demonstrate cutting-edge capabilities.
4. Responsive & Accessible
• Build a mobile-first responsive design using a 12-column grid.
• Follow best practices for HTML5 markup, CSS3, and lightweight JS (for countdown timer).
5. SEO & Technical Must-Haves
• Include basic SEO metadata and Open Graph tags.
• Provide a favicon placeholder.
• Placeholder for a Privacy Policy link in the footer.
Updates

Designs look the same

Industry/Entity Type

VARNEK Consulting Services is a boutique IT consultancy specializing in enterprise cloud solutions, microservices, FlowMesh migrations, and AGENTIC AI-driven integrations.

Coding

Coded - Design and coding required

Number of Pages Required

1 page

Requirements
Must have
• Below are our primary brand colors with hex codes (derived from CMYK values in the uploaded “Color and Font.jpg”): • Green (Globe Icon): #3BFF05 • Red (Q-Shape Icon): #EF1C03 • Blue (Circle Icon): #456EFF • Gold (Connector Icon): #F7C217 • Dark Gray / Text Color: #1A1A1A Use these colors for text highlights, buttons, icons, and accents. The overall page background is white or very light gray (#F9F9F9) to keep the design clean.
Should not have
• Colors outside the scheme provided

```html
<!DOCTYPE html>
<html lang="en">
<head>
<meta charset="utf-8">
<title>VARNEK Consulting Services — Coming Soon</title>
<link href="https://fonts.googleapis.com/css2?family=Open+Sans:wght@400;600;700&display=swap" rel="stylesheet">
<style>
:root{
  --blue:#456EFF;
  --gold:#F7C217;
  --red:#EF1C03;
  --green:#3BFF05;
  --ink:#1A1A1A;
  --light:#F9F9F9;
  --navy:#1c3570;
  --deep:#151b2b;
  --line:#d9dbe3;
}
*{box-sizing:border-box;margin:0;padding:0}
html,body{width:1200px;height:4535px;overflow:hidden}
body{font-family:"Open Sans",sans-serif;color:var(--ink);background:#fff;position:relative}
section,header,footer{position:relative;width:1200px;overflow:hidden}
.abs{position:absolute}
.btn{position:absolute;display:flex;align-items:center;justify-content:center;gap:6px;height:30px;border-radius:15px;font-size:10px;font-weight:600;letter-spacing:.3px;text-transform:uppercase;text-decoration:none}
.btn-blue{background:var(--blue);color:#fff}
.btn-gold{background:var(--gold);color:var(--ink)}
.btn-ghost{border:1.5px solid var(--gold);color:#fff}
.btn-outline{border:1.5px solid var(--blue);color:var(--ink);background:#fff}
.btn-white{background:#fff;color:var(--blue)}
.chev{font-size:12px;line-height:1}
.rule{display:inline-block;height:1px;background:var(--blue);vertical-align:middle}
.section-title{position:absolute;left:0;width:1200px;text-align:center;font-weight:600;font-size:29px;text-transform:uppercase;display:flex;align-items:center;justify-content:center;gap:16px}
.section-title .rule{width:68px}
.tick{display:inline-flex;width:14px;height:14px;border-radius:50%;background:var(--blue);flex:none;align-items:center;justify-content:center}
.checklist{position:absolute;list-style:none}
.checklist li{display:flex;gap:8px;align-items:flex-start;font-size:10.5px;line-height:14px}
.checklist b{font-weight:700;text-transform:uppercase}

/* hero */
.hero{height:618px;background:linear-gradient(100deg,#1b2f66 0%,#2455b8 45%,#3f8cf2 100%)}
.brand{display:flex;align-items:center;gap:8px;color:#fff}
.brand-dot{width:30px;height:30px;border-radius:50%;background:var(--blue);border:3px solid #fff}
.brand-name{font-size:22px;font-weight:700;line-height:1}
.brand-sub{font-size:8px;font-weight:400;line-height:1.2}
.nav{position:absolute;right:123px;top:38px;display:flex;align-items:center;gap:30px;font-size:10.5px;color:#fff;font-weight:600}
.nav .contact{background:var(--gold);color:var(--ink);padding:6px 18px;border-radius:13px}
.hero-kicker{left:121px;top:167px;font-size:10px;color:#fff;display:flex;align-items:center;gap:14px}
.hero-kicker .rule{width:100px;background:#8fb0ff}
.hero-title{left:121px;top:195px;font-size:30px;line-height:37px;font-weight:700;color:#fff;text-transform:uppercase}
.hero-sub{left:121px;top:272px;width:430px;font-size:13.5px;line-height:18px;color:#fff;font-weight:600}
.hero-copy{left:121px;top:343px;width:440px;font-size:10px;line-height:17px;color:#e4ecff}
.hero-art{left:600px;top:140px;width:520px;height:370px;border-radius:30px;background:radial-gradient(ellipse at center,#ffffff 0%,#cfe4ff 32%,rgba(80,150,255,.35) 65%,rgba(80,150,255,0) 80%)}
.mouse{left:593px;top:556px;width:14px;height:24px;border:2px solid #fff;border-radius:8px}
.mouse::after{content:"";position:absolute;left:4px;top:4px;width:2px;height:6px;background:#fff;border-radius:1px}

/* about */
.about{height:532px;background:#fff}
.about h2{left:121px;top:74px;font-size:29px;font-weight:700}
.about .rule{left:292px;top:95px;width:60px}
.about-copy{left:121px;top:116px;width:424px;font-size:10.5px;line-height:17.5px}
.why{left:121px;top:236px;font-size:12px;font-weight:700;display:flex;align-items:center;gap:10px}
.why .rule{width:70px}
.about .checklist{left:121px;top:268px;width:500px}
.about .checklist li{margin-bottom:13px}
.photo{border-radius:50%}

/* notify */
.notify{height:215px;background:linear-gradient(100deg,#3d62f2,var(--blue) 60%,#5a7fff)}
.notify .section-title{top:40px;color:#fff;font-size:27px;font-weight:600}
.notify .section-title .rule{background:#a9bcff;width:90px}
.email-field{left:273px;top:123px;width:533px;height:30px;border:1.5px solid var(--gold);border-radius:15px;padding-left:20px;display:flex;align-items:center;font-size:10px;color:#dfe6ff}

/* countdown */
.countdown{height:403px;background:#fff}
.countdown .section-title{top:54px}
.ring{position:absolute;top:129px;width:176px;height:176px}
.ring-num{position:absolute;top:181px;width:176px;text-align:center;font-size:46px;color:var(--red);font-weight:400}
.ring-label{position:absolute;top:327px;width:176px;text-align:center;font-size:13.5px;font-weight:600}

/* apart */
.apart{height:467px;background:linear-gradient(180deg,#1e2a44,#2b3b5e 60%,#1b2538)}
.apart-card{left:121px;top:64px;width:956px;height:341px;border:3px solid var(--blue);border-radius:12px;background:#fff;overflow:hidden}
.apart-card h2{position:absolute;left:33px;top:30px;font-size:29px;font-weight:600;display:flex;align-items:center;gap:10px}
.apart-card h2 .rule{width:70px}
.apart-card .checklist{left:33px;top:85px;width:400px}
.apart-card .checklist li{margin-bottom:13px}
.apart-photo{position:absolute;left:457px;top:0;width:496px;height:335px;background:linear-gradient(120deg,#3a3330,#8b7a70 40%,#e9e6e2 70%,#f4f3f1)}

/* services */
.services{height:457px;background:#fff}
.services .section-title{top:52px}
.svc{position:absolute;top:169px;width:307px;height:165px;background:#fff;border-radius:8px;box-shadow:0 2px 8px rgba(0,0,0,.14);text-align:center}
.svc-icon{position:absolute;left:121px;top:-32px;width:64px;height:64px;border-radius:50%;background:var(--blue);border:4px solid #dfe6ff;display:flex;align-items:center;justify-content:center}
.svc h3{margin-top:51px;font-size:11.5px;color:var(--blue);font-weight:600}
.svc p{margin:10px auto 0;width:270px;font-size:9.5px;line-height:14px}
.svc .more{margin-top:14px;font-size:10px;font-weight:700}
.svc .more span{color:var(--blue)}
.arrow-btn{position:absolute;width:28px;height:28px;border-radius:50%;border:1.5px solid var(--blue);color:var(--blue);display:flex;align-items:center;justify-content:center;font-size:14px;background:#fff}

/* value */
.value{height:356px;background:linear-gradient(90deg,#1d2433,#3a4156 50%,#1f2636)}
.value h2{position:absolute;left:0;width:1200px;text-align:center;top:54px;color:#fff;font-size:29px;font-weight:600}
.value .checklist{left:415px;top:116px;width:370px;color:#fff}
.value .checklist li{margin-bottom:12px}

/* agentic */
.agentic{height:431px;background:var(--light)}
.agentic .section-title{top:55px;font-size:29px}
.agentic-lead{left:0;width:1200px;top:96px;text-align:center;font-size:10.5px}
.ai-card{position:absolute;top:158px;width:468px;height:141px;background:#fff;border-radius:8px;box-shadow:0 2px 8px rgba(0,0,0,.14)}
.ai-icon{position:absolute;left:20px;top:22px;width:64px;height:64px;border-radius:50%;background:var(--blue);border:4px solid #dfe6ff;display:flex;align-items:center;justify-content:center}
.ai-card h3{position:absolute;left:103px;top:38px;font-size:13px;font-weight:600;color:var(--red);text-transform:uppercase}
.ai-card p{position:absolute;left:103px;top:64px;width:345px;font-size:10px;line-height:16px}

/* compare */
.compare{height:624px;background:#fff}
.compare h2{position:absolute;left:0;width:1200px;top:60px;text-align:center;font-size:28px;line-height:36px;font-weight:600;text-transform:uppercase}
.table{position:absolute;left:121px;top:209px;width:956px;border-collapse:collapse;font-size:13px}
.table th{background:var(--blue);color:#fff;font-weight:400;height:49px;text-transform:uppercase;border-right:1px solid #fff}
.table td{height:51px;border:1px solid var(--line);padding-left:14px}
.table td:first-child{text-align:center;padding-left:0}
.table th:nth-child(1){width:307px}
.table th:nth-child(2){width:343px}

/* schedule */
.schedule{height:247px;background:linear-gradient(100deg,#3d62f2,var(--blue) 60%,#5a7fff);color:#fff}
.schedule .section-title{top:52px;font-size:29px;font-weight:700;color:#fff}
.schedule .section-title .rule{background:#a9bcff;width:68px}
.schedule-copy{left:0;width:1200px;top:98px;text-align:center;font-size:10px;line-height:14px}

/* footer */
.footer{height:185px;background:var(--deep)}
.social{position:absolute;top:70px;width:36px;height:36px;border:1.5px solid #fff;border-radius:50%;display:flex;align-items:center;justify-content:center}
.legal{position:absolute;right:123px;top:67px;text-align:right;color:#fff;font-size:8px;line-height:20px}
</style>
</head>
<body>

<header class="hero">
  <div class="brand abs" style="left:121px;top:32px">
    <span class="brand-dot"></span>
    <div><div class="brand-name">VARNEK</div><div class="brand-sub">Consulting Services</div></div>
  </div>
  <nav class="nav">
    <span>HOME</span><span>ABOUT US ⌄</span><span>SERVICES ⌄</span><span>WORKS</span><span class="contact">CONTACT</span>
  </nav>
  <div class="hero-kicker abs">WELCOME TO VARNEK CONSULTING SERVICES <span class="rule"></span></div>
  <h1 class="hero-title abs">Enterprise Modernization<br>Reimagined</h1>
  <p class="hero-sub abs">Retire legacy systems and transition to secure, cloud-native infrastructure designed for scalability, AI integration, and future-ready performance.</p>
  <p class="hero-copy abs">Today's leaders don't have time for templated strategies and slow-moving firms. At VARNEK, we deliver tailored solutions that align with your business objectives, accelerate outcomes, and scale as you grow. Our senior experts work directly with your team to deliver fast, measurable impact-no layers, no delays. From modernizing legacy platforms to enabling intelligent automation, we solve the complex integration challenges others overlook so you can focus on leading the future</p>
  <a class="btn btn-blue" style="left:121px;top:474px;width:127px">Learn More</a>
  <a class="btn btn-ghost" style="left:260px;top:474px;width:129px">Get Started</a>
  <div class="hero-art abs" role="img" aria-label="Illustration of a cloud platform surrounded by floating app windows, documents and data panels"></div>
  <div class="mouse abs"></div>
</header>

<section class="about">
  <h2 class="abs">ABOUT US</h2>
  <span class="rule abs"></span>
  <p class="about-copy abs">Imagine a partner that doesn't hand you a recycled playbook-but builds a smarter path forward that's all about your goals. At VARNEK Consulting Services, we don't do cookie-cutter. We roll up our sleeves, work alongside your team, and deliver fast, measurable results that move the needle. While others push templates, we unlock possibilities-modern systems, real efficiency, and AI that actually works. No fluff. No junior handoffs. Just bold execution that gets you ahead and keeps you there</p>
  <div class="why abs">WHY WE'RE DIFFERENT <span class="rule"></span></div>
  <ul class="checklist">
    <li><span class="tick"><svg width="8" height="8" viewBox="0 0 8 8"><path d="M1 4l2 2 4-4" stroke="#fff" stroke-width="1.4" fill="none"/></svg></span><span><b>Senior Access, Always–</b> Speak directly to the experts. No junior full delays.</span></li>
    <li><span class="tick"><svg width="8" height="8" viewBox="0 0 8 8"><path d="M1 4l2 2 4-4" stroke="#fff" stroke-width="1.4" fill="none"/></svg></span><span><b>Speed That Scales–</b> Rapid execution means you see value faster—and scale without friction.</span></li>
    <li><span class="tick"><svg width="8" height="8" viewBox="0 0 8 8"><path d="M1 4l2 2 4-4" stroke="#fff" stroke-width="1.4" fill="none"/></svg></span><span><b>Elite Expertise, Zero Fluff–</b> Our DNA is Nimbus, FlowMesh, and bleeding-edge AI.</span></li>
    <li><span class="tick"><svg width="8" height="8" viewBox="0 0 8 8"><path d="M1 4l2 2 4-4" stroke="#fff" stroke-width="1.4" fill="none"/></svg></span><span><b>Custom Paths to Modernization–</b> Your transformation, built to fit and built to last.</span></li>
    <li><span class="tick"><svg width="8" height="8" viewBox="0 0 8 8"><path d="M1 4l2 2 4-4" stroke="#fff" stroke-width="1.4" fill="none"/></svg></span><span><b>Smarter Spend–</b> High impact. Low overhead. We outperform the big firms without<br>their price tags</span></li>
  </ul>
  <a class="btn btn-gold" style="left:121px;top:1052px;margin-top:-618px;width:127px;height:28px">Learn More <span class="chev">›</span></a>
  <svg class="abs" style="left:640px;top:55px" width="440" height="440" viewBox="0 0 440 440">
    <circle cx="249" cy="180" r="187" fill="none" stroke="var(--blue)" stroke-width="3"/>
  </svg>
  <div class="photo abs" style="left:704px;top:50px;width:366px;height:366px;background:linear-gradient(135deg,#5b6a5a,#2e3438 50%,#9c8c78)" role="img" aria-label="Photo of two businessmen in suits discussing work at a laptop"></div>
  <div class="photo abs" style="left:649px;top:236px;width:236px;height:236px;border:4px solid #fff;background:linear-gradient(135deg,#8da36a,#d9dccf 55%,#5d6d7d)" role="img" aria-label="Photo of a business team meeting around a table in a bright office"></div>
</section>

<section class="notify">
  <h2 class="section-title"><span class="rule"></span>BE THE FIRST TO KNOW WHEN WE GO LIVE<span class="rule"></span></h2>
  <div class="email-field abs">Enter your email</div>
  <a class="btn btn-white" style="left:818px;top:123px;width:109px;color:var(--ink)">Notify Me <span class="chev" style="color:var(--blue)">›</span></a>
</section>

<section class="countdown">
  <h2 class="section-title"><span class="rule"></span>COUNTDOWN TO LAUNCH<span class="rule"></span></h2>
  <svg class="ring" style="left:120px" viewBox="0 0 176 176"><circle cx="88" cy="88" r="84" fill="none" stroke="var(--ink)" stroke-width="4"/><circle cx="88" cy="88" r="84" fill="none" stroke="var(--blue)" stroke-width="4" stroke-dasharray="400 128" transform="rotate(-90 88 88)"/></svg>
  <div class="ring-num" style="left:120px">30</div><div class="ring-label" style="left:120px">DAYS</div>
  <svg class="ring" style="left:380px" viewBox="0 0 176 176"><circle cx="88" cy="88" r="84" fill="none" stroke="var(--ink)" stroke-width="4"/><circle cx="88" cy="88" r="84" fill="none" stroke="var(--blue)" stroke-width="4" stroke-dasharray="270 258" transform="rotate(0 88 88)"/></svg>
  <div class="ring-num" style="left:380px">00</div><div class="ring-label" style="left:380px">HOURS</div>
  <svg class="ring" style="left:640px" viewBox="0 0 176 176"><circle cx="88" cy="88" r="84" fill="none" stroke="var(--ink)" stroke-width="4"/><circle cx="88" cy="88" r="84" fill="none" stroke="var(--blue)" stroke-width="4" stroke-dasharray="260 268" transform="rotate(-20 88 88)"/></svg>
  <div class="ring-num" style="left:640px">00</div><div class="ring-label" style="left:640px">MINUTES</div>
  <svg class="ring" style="left:901px" viewBox="0 0 176 176"><circle cx="88" cy="88" r="84" fill="none" stroke="var(--ink)" stroke-width="4"/><circle cx="88" cy="88" r="84" fill="none" stroke="var(--blue)" stroke-width="4" stroke-dasharray="250 278" transform="rotate(-90 88 88)"/></svg>
  <div class="ring-num" style="left:901px">00</div><div class="ring-label" style="left:901px">SECONDS</div>
</section>

<section class="apart" role="img" aria-label="Dark background of business people silhouettes and market figures">
  <div class="apart-card abs">
    <h2>WHAT SETS US APART <span class="rule"></span></h2>
    <ul class="checklist">
      <li><span class="tick"><svg width="8" height="8" viewBox="0 0 8 8"><path d="M1 4l2 2 4-4" stroke="#fff" stroke-width="1.4" fill="none"/></svg></span><span><b>Tailored Execution</b> aligned directly with IT and business strategy</span></li>
      <li><span class="tick"><svg width="8" height="8" viewBox="0 0 8 8"><path d="M1 4l2 2 4-4" stroke="#fff" stroke-width="1.4" fill="none"/></svg></span><span><b>Accelerated ROI</b> and improved TCO metrics</span></li>
      <li><span class="tick"><svg width="8" height="8" viewBox="0 0 8 8"><path d="M1 4l2 2 4-4" stroke="#fff" stroke-width="1.4" fill="none"/></svg></span><span><b>Faster Turnaround Times</b> versus traditional consulting timelines</span></li>
      <li><span class="tick"><svg width="8" height="8" viewBox="0 0 8 8"><path d="M1 4l2 2 4-4" stroke="#fff" stroke-width="1.4" fill="none"/></svg></span><span><b>Direct Access to Experts—</b> no layers of junior consultants</span></li>
      <li><span class="tick"><svg width="8" height="8" viewBox="0 0 8 8"><path d="M1 4l2 2 4-4" stroke="#fff" stroke-width="1.4" fill="none"/></svg></span><span><b>Scalable, Secure Hybrid-Cloud Architectures</b> built to last</span></li>
      <li><span class="tick"><svg width="8" height="8" viewBox="0 0 8 8"><path d="M1 4l2 2 4-4" stroke="#fff" stroke-width="1.4" fill="none"/></svg></span><span><b>Embedded Agentic AI</b> for next-gen modernization intelligenc</span></li>
    </ul>
    <a class="btn btn-outline" style="left:33px;top:259px;width:122px;height:28px">View More <span class="chev" style="color:var(--blue)">›</span></a>
    <div class="apart-photo" role="img" aria-label="Photo of two businesswomen talking across a desk with a laptop"></div>
  </div>
</section>

<section class="services">
  <h2 class="section-title"><span class="rule"></span>OUR CORE SERVICES<span class="rule"></span></h2>
  <div class="arrow-btn" style="left:69px;top:237px">‹</div>
  <div class="arrow-btn" style="left:1101px;top:237px">›</div>
  <div class="svc" style="left:121px">
    <div class="svc-icon"><svg width="26" height="26" viewBox="0 0 26 26" fill="none" stroke="#fff" stroke-width="1.6"><path d="M13 2l10 6v10l-10 6-10-6V8z"/><path d="M13 8l5 3v5l-5 3-5-3v-5z"/></svg></div>
    <h3>Microservice Architectures</h3>
    <p>Fault-tolerant, scalable services that integrate with legacy systems—delivered faster than legacy consulting firms.</p>
    <div class="more">LEARN MORE <span>›</span></div>
  </div>
  <div class="svc" style="left:447px">
    <div class="svc-icon"><svg width="26" height="26" viewBox="0 0 26 26" fill="none" stroke="#fff" stroke-width="1.6"><circle cx="13" cy="11" r="7"/><path d="M6 21h14M9 24h8"/></svg></div>
    <h3>Nimbus Integration Architecture</h3>
    <p>Nimbus-native solutions tailored for your enterprise—built for scale, speed, and resilience.</p>
    <div class="more">LEARN MORE <span>›</span></div>
  </div>
  <div class="svc" style="left:771px">
    <div class="svc-icon"><svg width="26" height="26" viewBox="0 0 26 26" fill="none" stroke="#fff" stroke-width="1.6"><rect x="4" y="4" width="18" height="12" rx="2"/><path d="M9 20h8M13 16v4"/></svg></div>
    <h3>FlowMesh Migration &amp; Optimization</h3>
    <p>Minimized downtime. Maximized value. Precision-driven strategies over templates.</p>
    <div class="more">LEARN MORE <span>›</span></div>
  </div>
  <a class="btn btn-outline" style="left:517px;top:365px;width:164px;height:28px">View All Services <span class="chev" style="color:var(--blue)">›</span></a>
</section>

<section class="value" role="img" aria-label="Dark background of business leaders walking in front of city buildings">
  <h2>BUSINESS VALUE FOR ENTERPRISE LEADERSHIP</h2>
  <ul class="checklist">
    <li><span class="tick"><svg width="8" height="8" viewBox="0 0 8 8"><path d="M1 4l2 2 4-4" stroke="#fff" stroke-width="1.4" fill="none"/></svg></span><span><b>Efficiency:</b> Agile methods deliver faster results with less rework</span></li>
    <li><span class="tick"><svg width="8" height="8" viewBox="0 0 8 8"><path d="M1 4l2 2 4-4" stroke="#fff" stroke-width="1.4" fill="none"/></svg></span><span><b>Cost-Effectiveness:</b> Custom-fit solutions tailored to your enterprise</span></li>
    <li><span class="tick"><svg width="8" height="8" viewBox="0 0 8 8"><path d="M1 4l2 2 4-4" stroke="#fff" stroke-width="1.4" fill="none"/></svg></span><span><b>Scalability:</b> Cloud-native, legacy-compatible, and AI-optimized architectures</span></li>
    <li><span class="tick"><svg width="8" height="8" viewBox="0 0 8 8"><path d="M1 4l2 2 4-4" stroke="#fff" stroke-width="1.4" fill="none"/></svg></span><span><b>Security &amp; Compliance:</b> Built-in best practices from day one</span></li>
  </ul>
  <a class="btn btn-ghost" style="left:538px;top:268px;width:122px;height:28px">View More <span class="chev">›</span></a>
</section>

<section class="agentic">
  <h2 class="section-title"><span class="rule"></span>EMPOWERING MODERNIZATION WITH AGENTIC AI<span class="rule"></span></h2>
  <p class="agentic-lead abs">We embed AGENTIC AI into your workflows to deliver context-aware automation, autonomous monitoring, and real-time decisions.</p>
  <div class="arrow-btn" style="left:69px;top:213px">‹</div>
  <div class="arrow-btn" style="left:1101px;top:213px">›</div>
  <div class="ai-card" style="left:121px">
    <div class="ai-icon"><svg width="28" height="28" viewBox="0 0 28 28" fill="none" stroke="#fff" stroke-width="1.6"><circle cx="14" cy="14" r="5"/><path d="M14 3v4M14 21v4M3 14h4M21 14h4M6 6l3 3M19 19l3 3M6 22l3-3M19 9l3-3"/></svg></div>
    <h3>Autonomous Exception Handling</h3>
    <p>Agents monitor, classify, and route integration failures in real time—applying business rules or escalating only when needed. Outcome: reduced downtime, lower support overhead, and faster resolution.</p>
  </div>
  <div class="ai-card" style="left:609px">
    <div class="ai-icon"><svg width="28" height="28" viewBox="0 0 28 28" fill="none" stroke="#fff" stroke-width="1.6"><circle cx="14" cy="14" r="10"/><circle cx="14" cy="14" r="5"/><path d="M4 14h5M19 14h5"/></svg></div>
    <h3>Intelligent Data Enrichment</h3>
    <p>AI agents enrich payloads by referencing external sources (APIs,DBs, LLMs), auto-filling missing fields or standardizing formats before delivery. Outcome: cleaner data, reduced manual cleanup, faster processing.</p>
  </div>
  <a class="btn btn-blue" style="left:433px;top:339px;width:149px;height:28px">Schedule a Demo <span class="chev">›</span></a>
  <a class="btn btn-gold" style="left:596px;top:339px;width:171px;height:28px">Explore AI Use Cases <span class="chev">›</span></a>
</section>

<section class="compare">
  <h2>Smart IT and Business Leaders Are Moving Fast-<br>Here’s Why They’re Choosing Agile Over<br>Traditional Consulting</h2>
  <table class="table">
    <thead><tr><th>Aspect</th><th>VARNEK Consulting Services</th><th>Traditional Industry Giants</th></tr></thead>
    <tbody>
      <tr><td>Approach</td><td>Tailored, agile execution</td><td>Standardized, rigid frameworks</td></tr>
      <tr><td>Turnaround Time</td><td>Accelerated</td><td>Average to extended timelines</td></tr>
      <tr><td>Cost Efficiency</td><td>Transparent pricing</td><td>Premium costs &amp; overhead</td></tr>
      <tr><td>Expert Accessibility</td><td>Direct access to specialists</td><td>Layers of account managers</td></tr>
      <tr><td>Scalability Focus</td><td>Hyper-focused on your enterprise needs</td><td>Generic, one-size-fits-all solutions</td></tr>
      <tr><td>Innovation &amp; AI</td><td>Embedded AGENTIC AI &amp; adaptive<br>architectures</td><td>Legacy automation, limited adaptability</td></tr>
    </tbody>
  </table>
</section>

<section class="schedule">
  <h2 class="section-title"><span class="rule"></span>SCHEDULE A CONSULTATION<span class="rule"></span></h2>
  <p class="schedule-copy abs">Legacy isn't a roadmap. It's a roadblock. Let's architect what's next- secure, scalable, AI - enabled, and aligned with your business goals.<br>[Let's Reimagine Your Enterprise Together]</p>
  <a class="btn btn-white" style="left:537px;top:154px;width:125px;height:28px">Contact Us</a>
</section>

<footer class="footer">
  <div class="brand abs" style="left:121px;top:70px">
    <span class="brand-dot" style="width:40px;height:40px"></span>
    <div><div class="brand-name" style="font-size:26px">VARNEK</div><div class="brand-sub" style="font-size:9px">Consulting Services</div></div>
  </div>
  <div class="social" style="left:556px"><svg width="16" height="12" viewBox="0 0 16 12" fill="none" stroke="#fff" stroke-width="1.3"><rect x="1" y="1" width="14" height="10" rx="1"/><path d="M1 1l7 6 7-6"/></svg></div>
  <div class="social" style="left:607px" aria-label="Social profile"></div>
  <div class="legal">© 2025 VARNEK Consulting Services. All rights reserved.<br>Privacy| Terms &amp; Condition</div>
</footer>

</body>
</html>
```